Letterhead, stationery and email signature for construction business

I need the letterhead, stationery and email signature designs for a construction business. I want them to have a corporate feel to them.

I've attached the logo for reference.

```html
<!DOCTYPE html>
<html lang="en">
<head>
<meta charset="utf-8">
<title>Bravel Projects – Stationery</title>
<link rel="stylesheet" href="https://fonts.googleapis.com/css2?family=Arimo:wght@400;700&family=Questrial&display=swap">
<style>
  :root {
    --backdrop: #dcdcdc;
    --paper: #ffffff;
    --brand-blue: #2e55a3;
    --brand-slate: #4c4c58;
    --ink: #555555;
    --ink-dark: #3f3f46;
    --rule: #4c4c58;
    --sign-tone: #c9cbd1;
  }
  * { box-sizing: border-box; margin: 0; padding: 0; }
  html, body { width: 918px; height: 1200px; overflow: hidden; }
  body {
    position: relative;
    background: var(--backdrop);
    font-family: "Arimo", Arial, sans-serif;
    color: var(--ink);
  }

  /* ---------- Shared brand placeholder ---------- */
  .brand-mark {
    position: absolute; display: flex; align-items: center;
    font-family: "Arimo", Arial, sans-serif; font-weight: 400;
    color: var(--ink-dark); white-space: nowrap;
  }
  .brand-mark .brand-square { background: var(--brand-slate); flex: none; }

  .v-rule { position: absolute; width: 1px; background: var(--rule); }
  .contact-list { position: absolute; list-style: none; }
  .contact-list li { display: flex; align-items: center; color: var(--ink); white-space: nowrap; }
  .contact-list svg { flex: none; stroke: var(--brand-blue); fill: none; }

  /* ---------- Letterhead ---------- */
  .letterhead {
    position: absolute; left: 111px; top: 67px;
    width: 555px; height: 784px;
    background: var(--paper);
    overflow: hidden;
  }
  .letterhead .brand-mark { left: 49px; top: 42px; gap: 9px; }
  .letterhead .brand-square { width: 36px; height: 36px; }
  .letterhead .brand-name { font-size: 19px; }

  .letterhead .v-rule.first { left: 244px; top: 44px; height: 38px; }
  .letterhead .v-rule.second { left: 367px; top: 44px; height: 38px; }

  .address-block {
    position: absolute; left: 272px; top: 41px;
    font-size: 10px; line-height: 14.5px; color: var(--ink); font-style: normal;
  }
  .letterhead .contact-list { left: 391px; top: 41px; font-size: 10px; line-height: 14.5px; }
  .letterhead .contact-list li { gap: 5px; }
  .letterhead .contact-list svg { width: 8px; height: 8px; stroke-width: 1.6; }

  .letter-body { position: absolute; left: 49px; top: 240px; width: 456px; }
  .salutation {
    font-family: "Questrial", "Century Gothic", sans-serif;
    font-size: 13.5px; font-weight: 700; color: var(--ink-dark);
    margin-left: 1px; margin-bottom: 22px;
  }
  .letter-body p.para {
    font-size: 9.3px; line-height: 11.4px; color: var(--ink);
    margin-bottom: 10.3px;
  }
  .closing {
    font-family: "Questrial", "Century Gothic", sans-serif;
    font-size: 7.5px; font-weight: 700; color: var(--ink-dark);
    margin-top: 19px; margin-left: 1px;
  }
  .signature {
    display: block; width: 92px; height: 28px; margin-top: 20px;
    background: var(--sign-tone); border-radius: 3px;
  }
  .swoosh { position: absolute; left: 0; bottom: 0; display: block; }
  .swoosh .band { fill: var(--brand-blue); }
  .swoosh .stroke { fill: var(--brand-slate); }

  /* ---------- Business card ---------- */
  .business-card {
    position: absolute; left: 115px; top: 886px;
    width: 547px; height: 206px;
    background: var(--paper);
    overflow: hidden;
  }
  .business-card .brand-mark { left: 45px; top: 47px; gap: 11px; }
  .business-card .brand-square { width: 50px; height: 50px; }
  .business-card .brand-name { font-size: 25px; }
  .card-address {
    position: absolute; left: 46px; top: 116px;
    font-size: 13px; color: var(--ink);
  }
  .business-card .v-rule { left: 295px; top: 49px; height: 91px; }
  .holder { position: absolute; left: 318px; top: 44px; }
  .holder-name { font-size: 18.5px; font-weight: 700; color: var(--brand-blue); line-height: 1.1; }
  .holder-role { font-size: 13px; color: var(--ink); margin-top: 2px; }
  .business-card .contact-list { left: 318px; top: 89px; font-size: 13px; line-height: 19px; }
  .business-card .contact-list li { gap: 7px; }
  .business-card .contact-list svg { width: 11px; height: 11px; stroke-width: 1.5; }
</style>
</head>
<body>

<svg width="0" height="0" style="position:absolute" aria-hidden="true">
  <defs>
    <symbol id="icon-phone" viewBox="0 0 16 16"><path d="M4 2l2.5 3-1.5 1.5c.8 1.8 2.2 3.2 4 4L10.5 9l3 2.5-1.5 2C7 13.5 2.5 9 2.5 3.5z"/><path d="M10 2.5a4 4 0 0 1 3.5 3.5M10 5a1.5 1.5 0 0 1 1 1"/></symbol>
    <symbol id="icon-mail" viewBox="0 0 16 16"><rect x="1.5" y="3.5" width="13" height="9" rx="1"/><path d="M1.5 4.5L8 9l6.5-4.5"/></symbol>
    <symbol id="icon-globe" viewBox="0 0 16 16"><circle cx="8" cy="8" r="6.5"/><ellipse cx="8" cy="8" rx="3" ry="6.5"/><path d="M1.5 8h13M2.5 5h11M2.5 11h11"/></symbol>
  </defs>
</svg>

<section class="letterhead">
  <div class="brand-mark">
    <span class="brand-square"></span>
    <span class="brand-name">Bravel Projects</span>
  </div>
  <span class="v-rule first"></span>
  <address class="address-block">Your Address<br>City<br>State, Zip 0000</address>
  <span class="v-rule second"></span>
  <ul class="contact-list">
    <li><svg><use href="#icon-phone"/></svg>123-456-7800</li>
    <li><svg><use href="#icon-mail"/></svg>youremail@mailbox.com</li>
    <li><svg><use href="#icon-globe"/></svg>www.yourwebsite.com</li>
  </ul>

  <div class="letter-body">
    <p class="salutation">Dear Mr. Hartley,</p>
    <p class="para">Lorem ipsum dolor sit amet, consectetuer adipiscing elit, sed diam nonmmy nibh euismod tincidunt ut laor eet dolore magna aliquam erat volutpat. Ut wisi enim ad minim veniam, quis nostrud exerci tationmcorper suscipit lobortis nisl ut aliquip ex ea commodo consequat. Duis autem vel eum iriure dolor in hendrerit in vulputate velit esse molestie consequat, vel illum dolore eu feugiat</p>
    <p class="para">Rorem ipsum dolor sit amet, consectetuer adipiscing elit, sed diam nonmmy nibh euismod tincidunt ut laor eet dolore magna aliquam erat volutpat. Ut wisi enim ad minim veniam, quis nostrud exerci tationmcorper suscipit lobortis nisl ut aliquip ex ea commodo consequat. Duis autem vel eum iriure dolor in hendrerit in vulputate velit esse molest</p>
    <p class="para">Dorem ipsum dolor sit amet, consectetuer adipiscing elit, sed diam nonmmy nibh euismod tincidunt ut laor eet dolore magna aliquam erat volutpat. Ut wisi enim ad minim veniam, quis nostrud exerci tationmcorper suscipit lobortis nisl ut aliquip ex ea commodo consequat. Duis autem vel eum iriure dolor in hendrerit in suscipit lobortis nisl ut aliquip ex ea commodo consequat. Duis autem vel eum iriure dolor in hendrerit in vulputate velit esse molestie consequat, vel illum</p>
    <p class="para">Sorem ipsum dolor sit amet, consectetuer adipiscing elit, sed diam nonmmy nibh euismod tincidunt ut laor eet dolore magna aliquam erat volutpat. Ut wisi enim ad minim veniam, quis nostrud exerci tationmcorper suscipit lobortis nisl ut aliquip ex ea commodo consequat. Duis autem vel eum iriure dolor in</p>
    <p class="closing">Sincerely,</p>
    <span class="signature" role="img" aria-label="Handwritten signature of the sender"></span>
  </div>

  <svg class="swoosh" width="555" height="70" viewBox="0 0 555 70" aria-hidden="true">
    <path class="band" d="M0 39 C150 62 350 58 555 20 L555 70 L0 70 Z"/>
    <path class="stroke" d="M91 46 C300 58 450 34 555 0 L555 15 C450 44 300 62 91 46 Z"/>
  </svg>
</section>

<section class="business-card">
  <div class="brand-mark">
    <span class="brand-square"></span>
    <span class="brand-name">Bravel Projects</span>
  </div>
  <p class="card-address">Your Address, City, State, Zip 0000</p>
  <span class="v-rule"></span>
  <div class="holder">
    <p class="holder-name">DANIEL HARTLEY</p>
    <p class="holder-role">Manager</p>
  </div>
  <ul class="contact-list">
    <li><svg><use href="#icon-phone"/></svg>123-456-7800</li>
    <li><svg><use href="#icon-mail"/></svg>youremail@mailbox.com</li>
    <li><svg><use href="#icon-globe"/></svg>www.yourwebsite.com</li>
  </ul>
  <svg class="swoosh" width="547" height="70" viewBox="0 0 547 70" aria-hidden="true">
    <path class="band" d="M0 39 C150 62 350 58 547 23 L547 70 L0 70 Z"/>
    <path class="stroke" d="M90 46 C300 58 450 32 547 2 L547 16 C450 44 300 62 90 46 Z"/>
  </svg>
</section>

</body>
</html>
```